Vexo QR

Create flyers for product information
https://vexo-qr.examplestore.test/
Our products are 100% plant extracts
2 patients.
Our base product starts with human homeopathy formula and with the same team of doctors, created vexo-QR.
It’s produced in a laboratory that is certified human grade.
Our standard meets and exceeds all EU and USA requirements
Trials include a university in Germany.
On farms trials, in Asia, Europe, USA,
Australia and Canada.
No milk and meat withdrawals.
It’s produced in The Netherlands. And we meet U.S. and European standards.
3 different types of vexo-QR (for flyer design each):
Package 1
10 doses ready to use ( RTU )
25 mL. Per dose 10 Pipettes 1 bottle of 250 mL vexo-QR. 1 35 ML syringe.
Package 2
33 doses concentrated Vexo-QR.
250 ML bottle of concentrated vexo QR.
33 Pipettes, 1 35 ML syringe.
Mix the full amount of the 250 ML bottle along with 750 mL of sterile saline Solution. Making 1000mL
A 30 ML dose per cow.
Package 3
HORSE
Single dose package of a 40 ML dose RTU.
1 Pipette, 1 40, ML bottle of vexo-QR.
1 syringe.

```html
<!DOCTYPE html>
<html lang="en">
<head>
<meta charset="utf-8">
<title>Vexo QR – Intra Uterine Infusion Wash Flyer</title>
<link rel="stylesheet" href="https://fonts.googleapis.com/css2?family=Montserrat:ital,wght@0,400;0,500;0,800;1,800&family=Barlow+Semi+Condensed:wght@700&family=Baloo+2:wght@800&family=Arimo&display=swap">
<style>
  :root {
    --backdrop: #c4c4c4;
    --paper: #ffffff;
    --green: #009a54;
    --green-light: #6cbf6a;
    --leaf: #5cb85c;
    --navy: #2d3441;
    --red: #ee3e3a;
    --ink: #2b2f3a;
  }
  * { margin: 0; padding: 0; box-sizing: border-box; }
  html, body { width: 1043px; height: 1200px; overflow: hidden; background: var(--backdrop); }
  .flyer {
    position: absolute; left: 174px; top: 108px;
    width: 695px; height: 984px; background: var(--paper); overflow: hidden;
    font-family: "Montserrat", sans-serif; color: var(--ink);
  }
  .layer { position: absolute; left: 0; top: 0; }
  .headline {
    position: absolute; left: 57px; top: 0; width: 590px; height: 125px;
    background: var(--green); border-radius: 0 0 12px 12px;
    color: #fff; text-align: center;
  }
  .headline-kicker {
    display: block; margin-top: 10px; font-style: italic; font-weight: 800;
    font-size: 44px; line-height: 46px; letter-spacing: 3px;
  }
  .headline-main {
    display: block; font-weight: 800; font-size: 56px; line-height: 56px; letter-spacing: 4px;
  }
  .brand-card {
    position: absolute; left: 501px; top: 264px; width: 161px; height: 170px;
    background: var(--paper); border-radius: 10px 10px 0 0;
    text-align: center;
  }
  .brand-dot {
    width: 48px; height: 48px; border-radius: 50%; background: var(--navy);
    margin: 38px auto 0;
  }
  .brand-name {
    position: absolute; left: 0; right: 0; top: 130px;
    font-weight: 500; font-size: 25px; letter-spacing: 1px; color: var(--ink);
  }
  .claim {
    position: absolute; left: 20px; top: 486px; width: 265px; text-align: center;
    font-family: "Barlow Semi Condensed", sans-serif; font-weight: 700; color: var(--green);
  }
  .claim-main { display: block; font-size: 39px; line-height: 38px; letter-spacing: -0.5px; }
  .claim-sub { display: block; font-size: 29px; line-height: 30px; }
  .plant-badge {
    position: absolute; left: 57px; top: 589px; width: 206px; height: 84px;
    background: var(--navy); border-radius: 10px;
  }
  .plant-badge .leaf-icon {
    position: absolute; left: 12px; top: 10px; width: 60px; height: 64px;
    background: linear-gradient(135deg, #7fd07c, #1fa24e); border-radius: 50% 0 50% 50%;
  }
  .plant-badge .rule { position: absolute; left: 82px; top: 12px; width: 1px; height: 60px; background: #fff; }
  .plant-badge .badge-text {
    position: absolute; left: 92px; top: 8px;
    font-family: "Baloo 2", sans-serif; font-weight: 800; font-size: 21px; line-height: 20px; color: var(--leaf);
  }
  .plant-badge .badge-text b { color: #fff; font-weight: 800; }
  .benefits { position: absolute; left: 332px; top: 488px; width: 340px; list-style: none; }
  .benefits li {
    position: relative; padding-left: 21px; font-size: 10.2px; line-height: 12.5px; margin-bottom: 8.5px;
  }
  .benefits svg { position: absolute; left: 0; top: 1px; width: 12px; height: 10px; }
  .product-shot {
    position: absolute; left: 33px; top: 699px; width: 285px; height: 265px;
    background: linear-gradient(160deg, #f4f4f4 0%, #e6e6e6 55%, #cfcfcf 100%);
    border-radius: 4px;
  }
  .package {
    position: absolute; left: 351px; top: 673px; width: 282px; height: 253px;
    border-radius: 10px; overflow: hidden; background: var(--green-light);
    color: #fff; text-align: center;
  }
  .package-title {
    height: 102px; background: var(--green);
    font-family: "Montserrat", sans-serif; font-weight: 800; font-size: 28px; line-height: 28px;
    padding-top: 23px; letter-spacing: 0.5px;
  }
  .package-contents { font-family: "Arimo", sans-serif; font-size: 18.5px; line-height: 22px; }
  .package-contents p { margin: 0 33px; padding: 5px 0 5px; border-bottom: 1px solid #fff; }
  .package-contents p:first-child { padding-top: 7px; }
  .package-contents p:last-child { border-bottom: none; }
  .web-address {
    position: absolute; left: 328px; top: 946px; width: 330px;
    font-size: 13px; font-weight: 500; letter-spacing: 2.2px; color: #fff; white-space: nowrap;
  }
  .web-address span { color: var(--green-light); font-weight: 800; }
</style>
</head>
<body>
<main class="flyer">
  <svg class="layer" width="695" height="984" viewBox="0 0 695 984" aria-hidden="false">
    <defs>
      <linearGradient id="pastureTone" x1="0" y1="0" x2="0" y2="1">
        <stop offset="0" stop-color="#4d4a48"/>
        <stop offset="0.38" stop-color="#6b6a5e"/>
        <stop offset="0.55" stop-color="#7fb84a"/>
        <stop offset="1" stop-color="#5fa332"/>
      </linearGradient>
    </defs>
    <path role="img" aria-label="Photo of Holstein dairy cows grazing on a green pasture in front of farm buildings"
          d="M0 0 H695 V341 Q350 520 0 350 Z" fill="url(#pastureTone)"/>
    <path d="M0 350 Q350 520 695 341 V352 Q380 535 0 380 Z" fill="var(--navy)"/>
    <path d="M0 380 Q220 470 400 440 Q220 480 0 398 Z" fill="var(--red)"/>
    <path d="M0 888 Q160 970 380 950 Q560 930 695 880 V984 H0 Z" fill="var(--navy)"/>
    <path d="M280 955 Q520 930 695 850 V872 Q520 945 300 958 Z" fill="var(--red)"/>
  </svg>

  <header class="headline">
    <span class="headline-kicker">An intra uterine</span>
    <span class="headline-main">INFUSION WASH</span>
  </header>

  <div class="brand-card">
    <div class="brand-dot"></div>
    <div class="brand-name">VEXO QR</div>
  </div>

  <h2 class="claim">
    <span class="claim-main">ANTIBIOTIC FREE</span>
    <span class="claim-sub">FOR CATLLE</span>
  </h2>

  <div class="plant-badge">
    <div class="leaf-icon" role="img" aria-label="Green leaf illustration"></div>
    <div class="rule"></div>
    <div class="badge-text"><b>100%</b><br>PLANT<br>EXTRACTS</div>
  </div>

  <ul class="benefits">
    <li><svg viewBox="0 0 12 10"><path d="M1 5 L4.5 8.5 L11 1.5" fill="none" stroke="#ee3e3a" stroke-width="2"/></svg>Base product starts with human homeopathy formula and with the same team of doctors, created vexo-QR.</li>
    <li><svg viewBox="0 0 12 10"><path d="M1 5 L4.5 8.5 L11 1.5" fill="none" stroke="#ee3e3a" stroke-width="2"/></svg>Produced in a laboratory that is certified human grade.</li>
    <li><svg viewBox="0 0 12 10"><path d="M1 5 L4.5 8.5 L11 1.5" fill="none" stroke="#ee3e3a" stroke-width="2"/></svg>Standard meets &amp; exceeds all EU and USA requirements</li>
    <li><svg viewBox="0 0 12 10"><path d="M1 5 L4.5 8.5 L11 1.5" fill="none" stroke="#ee3e3a" stroke-width="2"/></svg>Trials include a university in Germany.</li>
    <li><svg viewBox="0 0 12 10"><path d="M1 5 L4.5 8.5 L11 1.5" fill="none" stroke="#ee3e3a" stroke-width="2"/></svg>On farms trials, in Asia, Europe, USA, Australia &amp; Canada.</li>
    <li><svg viewBox="0 0 12 10"><path d="M1 5 L4.5 8.5 L11 1.5" fill="none" stroke="#ee3e3a" stroke-width="2"/></svg>No milk and meat withdrawals.</li>
    <li><svg viewBox="0 0 12 10"><path d="M1 5 L4.5 8.5 L11 1.5" fill="none" stroke="#ee3e3a" stroke-width="2"/></svg>Produced in The Netherlands &amp; we meet U.S.<br>and European standards.</li>
  </ul>

  <div class="product-shot" role="img" aria-label="Product photo: white packaging boxes, amber bottle, pipette and syringe"></div>

  <section class="package">
    <h3 class="package-title">10 DOSES<br>READY TO USE</h3>
    <div class="package-contents">
      <p>25 mL. Per dose<br>10 Pipettes</p>
      <p>1 bottle of 250 mL<br>vexo-QR.</p>
      <p>1 35 ML syringe.</p>
    </div>
  </section>

  <div class="web-address">www.<span>vexo-qr.examplestore</span>.test</div>
</main>
</body>
</html>
```